New Tech Support Service needs a website design

We need a web design for a new product we are developing that provides tech support to consumers for a small ongoing monthly fee. We are looking for a fresh, technology look and feel. We want the site to have a tech feel - yet not intimidating. Simple and welcoming. We are in need of an initial landing page, sign on page, and a product home page.

Thank you to everyone who submitted designs. It was a very difficult decision!

Industry/Entity Type

Tech

```html
<!DOCTYPE html>
<html lang="en">
<head>
<meta charset="utf-8">
<title>Tech Support Service</title>
<link href="https://fonts.googleapis.com/css2?family=Lato:wght@300;400;700;900&display=swap" rel="stylesheet">
<style>
:root{
  --blue:#1fa9e1;
  --blue-dark:#1590c4;
  --ink:#2a2a2a;
  --text:#555;
  --topbar:#2b2d30;
  --slate:#3a5563;
  --light:#eef1f3;
  --footer:#1c1d1f;
  --white:#fff;
}
*{margin:0;padding:0;box-sizing:border-box}
html,body{width:1200px;height:2595px;overflow:hidden;background:var(--white)}
body{font-family:'Lato',Arial,sans-serif;color:var(--text);position:relative}
.abs{position:absolute}

/* top bar */
.topbar{left:0;top:0;width:1200px;height:45px;background:var(--topbar);color:#fff;font-size:14px}
.topbar .call{position:absolute;left:152px;top:14px}
.topbar .social{position:absolute;left:862px;top:8px;display:flex;gap:8px}
.topbar .social span{width:28px;height:28px;border-radius:50%;border:2px solid #fff;display:block}
.topbar .signin{position:absolute;left:975px;top:8px;width:60px;height:28px;background:var(--blue);color:#fff;font-size:14px;font-weight:700;text-align:center;line-height:28px}

/* nav */
.nav{left:0;top:45px;width:1200px;height:72px;background:var(--white);box-shadow:0 2px 4px rgba(0,0,0,.08)}
.brand{position:absolute;left:152px;top:20px;font-size:28px;font-weight:700;color:var(--ink)}
.menu{position:absolute;left:571px;top:0;display:flex;height:72px;font-size:14px;color:var(--ink)}
.menu a{display:block;line-height:72px;padding:0 16px;color:inherit;text-decoration:none}
.menu a.active{background:var(--blue);color:#fff}

/* hero */
.hero{left:0;top:117px;width:1200px;height:483px;background:linear-gradient(120deg,#5d6d7c 0%,#9aa6b1 35%,#c9d0d6 55%,#7c8994 80%,#4c5865 100%)}
.hero h1{position:absolute;left:0;top:166px;width:1200px;text-align:center;color:#fff;font-size:36px;font-weight:700;line-height:50px;letter-spacing:.5px;text-shadow:0 2px 6px rgba(0,0,0,.35)}
.hero .btn{position:absolute;left:493px;top:333px;width:214px;height:44px;background:#222;color:#fff;font-size:22px;font-weight:700;text-align:center;line-height:44px}

/* features */
.features{left:0;top:600px;width:1200px;height:168px;background:var(--blue)}
.feature{position:absolute;top:30px;width:160px;text-align:center;color:#fff;font-size:13px}
.feature .tile{width:66px;height:66px;background:#fff;margin:0 auto 12px;display:flex;align-items:center;justify-content:center;box-shadow:0 3px 0 rgba(0,0,0,.15)}

/* about */
.about-photo{left:130px;top:790px;width:405px;height:313px;background:linear-gradient(180deg,#e7eaed,#b9c0c7 60%,#6d757d)}
.section-h{font-weight:400;color:var(--ink);letter-spacing:1px}
.about h2{position:absolute;left:584px;top:800px;font-size:44px}
.about .lead{position:absolute;left:584px;top:860px;width:448px;height:26px;background:var(--blue);color:#fff;font-size:13px;line-height:26px;padding-left:10px}
.about p{position:absolute;left:584px;top:900px;width:448px;font-size:12.5px;line-height:16px;color:var(--text)}

/* service */
.service{left:0;top:1103px;width:1200px;height:497px;background:var(--slate);color:#fff;text-align:center}
.service h2{position:absolute;left:0;top:40px;width:1200px;font-size:44px;font-weight:400;letter-spacing:1px}
.service .sub,.work .sub{position:absolute;left:0;width:1200px;text-align:center;font-size:16px}
.service .sub{top:104px}
.card{position:absolute;top:168px;width:246px;text-align:center}
.card .photo{width:246px;height:168px;border:6px solid #fff;box-shadow:0 4px 8px rgba(0,0,0,.3)}
.card h3{margin-top:18px;font-size:24px;font-weight:400;color:var(--blue)}
.card p{margin-top:4px;font-size:13px;line-height:16px;color:#dfe6ea}
.card .more{display:block;margin-top:22px;font-size:12px;color:#fff}

/* work */
.work{left:0;top:1600px;width:1200px;height:540px;background:linear-gradient(180deg,#f4f6f7,#e2e7ea)}
.work h2{position:absolute;left:0;top:38px;width:1200px;text-align:center;font-size:44px}
.work .sub{top:102px;color:var(--text)}
.work p{position:absolute;left:162px;top:177px;width:430px;font-size:14px;line-height:18px;color:#333}
.work .more{position:absolute;left:162px;top:408px;font-size:12px;color:#333}
.devices{left:610px;top:1752px;width:510px;height:360px;background:radial-gradient(ellipse at 50% 55%,#f8fafb 0%,#c8d1d8 55%,#9aa6b0 100%);border-radius:6px}

/* testimonial */
.testi h2{position:absolute;left:0;top:2175px;width:1200px;text-align:center;font-size:44px}
.person{top:2290px;width:120px;height:175px;background:linear-gradient(180deg,#eceff1,#aab2b9 55%,#4f5760)}
.quote{top:2330px;width:260px}
.quote h4{font-size:24px;font-weight:400;color:var(--ink)}
.quote p{margin-top:8px;font-size:13px;line-height:16px;color:var(--text)}
.divider{left:584px;top:2290px;width:1px;height:160px;background:#d6d9dc}

/* footer */
.footnav{left:0;top:2465px;width:1200px;height:48px;background:var(--blue);color:#fff;font-size:14px}
.footnav .links{position:absolute;left:188px;top:0;display:flex;gap:34px;line-height:48px}
.footnav .follow{position:absolute;left:827px;top:0;line-height:48px;font-size:15px}
.footnav .squares{position:absolute;left:912px;top:10px;display:flex;gap:8px}
.footnav .squares span{width:28px;height:28px;background:#fff;opacity:.9;display:block}
.copyright{left:0;top:2513px;width:1200px;height:82px;background:var(--footer);color:#aaa;font-size:12px;text-align:center;line-height:82px}
</style>
</head>
<body>

<header class="abs topbar">
  <span class="call">Call us : 0100-5550199</span>
  <div class="social"><span></span><span></span><span></span></div>
  <span class="signin">Sign in</span>
</header>

<nav class="abs nav">
  <div class="brand">Tech Support Service</div>
  <div class="menu">
    <a class="active">Home</a><a>About Us</a><a>Service</a><a>Our Work</a><a>Product</a><a>Reach Us</a>
  </div>
</nav>

<section class="abs hero" role="img" aria-label="Photo of a business person using a tablet">
  <h1>LOREM IPSUM DOLOR SIT AMET, CONSECTETUER<br>ADIPISCING ELIT</h1>
  <div class="btn">LOREM IPSUM</div>
</section>

<section class="abs features">
  <div class="feature" style="left:196px">
    <div class="tile"><svg width="34" height="30" viewBox="0 0 34 30"><rect x="2" y="2" width="30" height="19" fill="none" stroke="#2a2a2a" stroke-width="3"/><rect x="14" y="21" width="6" height="5" fill="#2a2a2a"/><rect x="9" y="26" width="16" height="3" fill="#2a2a2a"/></svg></div>
    Lorem Ipsum Dolo
  </div>
  <div class="feature" style="left:400px">
    <div class="tile"><svg width="22" height="34" viewBox="0 0 22 34"><rect x="2" y="2" width="18" height="30" rx="3" fill="none" stroke="#2a2a2a" stroke-width="3"/><circle cx="11" cy="27" r="2" fill="#2a2a2a"/></svg></div>
    Lorem Ipsum Dolo
  </div>
  <div class="feature" style="left:604px">
    <div class="tile"><svg width="32" height="32" viewBox="0 0 32 32"><g fill="#2a2a2a"><rect x="13" y="1" width="6" height="30"/><rect x="1" y="13" width="30" height="6"/><rect x="13" y="1" width="6" height="30" transform="rotate(45 16 16)"/><rect x="13" y="1" width="6" height="30" transform="rotate(-45 16 16)"/><circle cx="16" cy="16" r="10"/></g><circle cx="16" cy="16" r="4" fill="#fff"/></svg></div>
    Lorem Ipsum Dolo
  </div>
  <div class="feature" style="left:812px">
    <div class="tile"><svg width="30" height="32" viewBox="0 0 30 32"><circle cx="15" cy="9" r="7" fill="#2a2a2a"/><path d="M2 31c0-9 6-13 13-13s13 4 13 13z" fill="#2a2a2a"/></svg></div>
    Lorem Ipsum Dolo
  </div>
</section>

<div class="abs about-photo" role="img" aria-label="Photo of two smiling business colleagues"></div>
<section class="about">
  <h2 class="section-h">ABOUT US</h2>
  <div class="lead">Sed ut perspiciatis unde omnis iste natus error</div>
  <p>Sed ut perspiciatis unde omnis iste natus error sit voluptatem accusantium doloremque laudantium, totam rem aperiam, eaque ipsa quae ab illo inventore veritatis et quasi architecto beatae vitae dicta sunt explicabo. Nemo enim ipsam voluptatem quia voluptas sit aspernatur aut odit aut fugit, sed quia consequuntur magni dolores eos qui ratione voluptatem sequi nesciunt. Sed ut perspiciatis unde omnis iste natus error sit voluptatem accusantium doloremque laudantium, totam rem aperiam, eaque ipsa quae ab illo inventore veritatis et quasi architecto beatae vitae dicta sunt explicabo.</p>
</section>

<section class="abs service">
  <h2>SERVICE</h2>
  <div class="sub">Sed ut perspiciatis unde omnis iste natus error sit voluptatem accusantium doloremque</div>
  <div class="card" style="left:169px">
    <div class="photo" role="img" aria-label="Photo of a business team" style="background:linear-gradient(180deg,#dfe3e6,#8e979f)"></div>
    <h3>LOREM IPSUM</h3>
    <p>Sed ut perspiciatis unde omnis iste<br>natus error sit voluptatem accusantium<br>doloremque</p>
    <span class="more">Read more</span>
  </div>
  <div class="card" style="left:477px">
    <div class="photo" role="img" aria-label="Photo of a business handshake" style="background:linear-gradient(180deg,#7fa6c8,#c9d3db 60%,#6c7882)"></div>
    <h3>LOREM IPSUM</h3>
    <p>Sed ut perspiciatis unde omnis iste<br>natus error sit voluptatem accusantium<br>doloremque</p>
    <span class="more">Read more</span>
  </div>
  <div class="card" style="left:785px">
    <div class="photo" role="img" aria-label="Photo of a hand pointing at a rising chart" style="background:linear-gradient(135deg,#e9edf0,#a9b6c2 50%,#a8464a)"></div>
    <h3>LOREM IPSUM</h3>
    <p>Sed ut perspiciatis unde omnis iste<br>natus error sit voluptatem accusantium<br>doloremque</p>
    <span class="more">Read more</span>
  </div>
</section>

<section class="abs work">
  <h2 class="section-h">OUR WORK</h2>
  <div class="sub">Sed ut perspiciatis unde omnis iste natus error sit voluptatem accusantium doloremque</div>
  <p>Sed ut perspiciatis unde omnis iste natus error sit voluptatem accusantium doloremque laudantium, totam rem aperiam, eaque ipsa quae ab illo inventore veritatis et quasi architecto beatae vitae dicta sunt explicabo. Nemo enim ipsam voluptatem quia voluptas sit aspernatur aut odit aut fugit, sed quia consequuntur magni dolores eos qui ratione voluptatem sequi nesciunt. Neque porro quisquam est, qui dolorem ipsum quia dolor sit amet, consectetur, adipisci velit, sed quia non numquam.</p>
  <span class="more">Read more</span>
</section>
<div class="abs devices" role="img" aria-label="Website shown on a desktop monitor, laptop, tablet and phone"></div>

<section class="testi">
  <h2 class="section-h">TESTIMONIAL</h2>
  <div class="abs person" style="left:162px" role="img" aria-label="Portrait of a smiling businesswoman"></div>
  <div class="abs quote" style="left:298px">
    <h4>Sed Ut Perspicialis</h4>
    <p>"Sed ut perspiciatis unde omnis iste natus error sit voluptatem accusantium doloremque laudantium. "</p>
  </div>
  <div class="abs divider"></div>
  <div class="abs person" style="left:665px" role="img" aria-label="Portrait of a smiling businessman"></div>
  <div class="abs quote" style="left:801px">
    <h4>Sed Ut Perspicialis</h4>
    <p>"Sed ut perspiciatis unde omnis iste natus error sit voluptatem accusantium doloremque laudantium. "</p>
  </div>
</section>

<footer class="abs footnav">
  <div class="links"><span>Home</span><span>About Us</span><span>Service</span><span>Our Work</span><span>Product</span><span>Reach Us</span></div>
  <span class="follow">Follow Us</span>
  <div class="squares"><span></span><span></span><span></span><span></span></div>
</footer>
<div class="abs copyright">Copyright Privacy | 2016</div>

</body>
</html>
```